Modern, eye catching eliquid bottle label. 1.5 x 2.75

We need a label design for our e-juice bottles. The labels to be printed are 1.5 inches in height and 2.75 inches in width. We are looking to include our website (www.quillbrookmistparlor.com) and our phone number of 2 different shops. The most prominent thing needs to be our logo(attached .pdf and jpeg). We will need 2 spots that we can edit on an ongoing basis for nicotine strength and the flavor. We want something simplistic but eye-catching. Our colors are Purple, Red, and Orange. We would also like our website fairly prominent as well.

Target Market(s)

18-45 vapers and e-cigarette users

Font styles to use
Serif

Colors
6b449b
f78e1f
ec1f27
ffffff
000000

Requirements
Must have
• eye catching
• "Quillbrook Mist" must be LARGE
• phone number
• website
• areas for flavor name and nicotine strength
• orange, purple, black and red
Nice to have
• clean, abstract vectors
• "corporate look"
• think of a DUNTRA FIZZ can, you immediately know what your'e looking at.
• Our V in vapor is our go to logo
Should not have
• no grunge effects
• no round shapes

```html
<!DOCTYPE html>
<html lang="en">
<head>
<meta charset="utf-8">
<title>Quillbrook Mist – Bottle Label Concepts</title>
<link rel="stylesheet" href="https://fonts.googleapis.com/css2?family=Playfair+Display:ital,wght@1,700&family=Righteous&display=swap">
<style>
  :root {
    --paper: #ffffff;
    --sheet-edge: #d9d9d9;
    --trim: #000000;
    --label-dark: #363636;
    --label-mid: #484848;
    --band-deep: #1c1c1c;
    --ink-light: #ffffff;
    --brand-purple-bright: #b57ee8;
    --flavor-green: #8dc63f;
    --divider: #9a9a9a;
    --mist-a: rgba(255,255,255,0.14);
    --mist-b: rgba(255,255,255,0);
  }
  html, body { margin: 0; padding: 0; overflow: hidden; }
  body { width: 1200px; height: 813px; background: var(--paper); }
  .sheet {
    position: relative; width: 1200px; height: 813px; box-sizing: border-box;
    border: 1px solid var(--sheet-edge); background: var(--paper);
  }
  .label { position: absolute; box-sizing: border-box; }
  .label--trim { border: 1px solid var(--trim); background: var(--paper); }
  .label--wrap { background: var(--label-mid); border: 1px solid #2a2a2a; }

  .face { position: absolute; top: 0; bottom: 0; overflow: hidden; }
  .label--trim .face { left: 78px; width: 287px; background: var(--label-dark); }
  .label--wrap .face { left: 78px; width: 287px; background: var(--label-mid); }

  .mist {
    position: absolute; left: 0; right: 0; top: 0; bottom: 0;
    background: radial-gradient(ellipse 70% 55% at 45% 45%, var(--mist-a), var(--mist-b) 75%);
  }
  .band { position: absolute; left: 0; right: 0; height: 50px; }
  .band--top { top: 0; background: linear-gradient(to bottom, var(--band-deep), rgba(28,28,28,0)); }
  .band--bottom { bottom: 0; background: linear-gradient(to top, var(--band-deep), rgba(28,28,28,0)); }

  .web {
    position: absolute; left: 0; right: 0; text-align: center; color: var(--ink-light);
    font-family: Arial, Helvetica, sans-serif; font-weight: bold; white-space: nowrap;
  }
  .label--trim .web { bottom: 16px; font-size: 15px; }
  .label--wrap .web { top: 8px; font-size: 12.5px; }

  .brand {
    position: absolute; left: 0; right: 0; text-align: center; white-space: nowrap;
    font-family: "Playfair Display", Georgia, serif; font-style: italic; font-weight: 700;
    color: var(--brand-purple-bright);
  }
  .label--trim .brand { top: 88px; font-size: 38px; }
  .label--wrap .brand { top: 80px; font-size: 32px; }

  .flavor {
    position: absolute; left: 0; right: 0; top: 138px; text-align: center;
    font-family: "Righteous", Impact, sans-serif; font-size: 40px; letter-spacing: 2px;
    color: var(--flavor-green);
  }

  .phones {
    position: absolute; bottom: 8px; left: 0; right: 0; display: flex;
    justify-content: space-around; align-items: center;
    font-family: "Playfair Display", Georgia, serif; font-style: italic;
    font-variant-numeric: lining-nums;
    font-size: 13px; color: var(--ink-light);
  }
  .phones .rule { width: 1px; height: 18px; background: var(--divider); }
</style>
</head>
<body>
<main class="sheet">

  <section class="label label--trim" style="left:86px; top:105px; width:443px; height:243px;">
    <div class="face">
      <div class="mist" role="img" aria-label="Soft drifting smoke wisps"></div>
      <div class="band band--bottom"></div>
      <div class="brand">Quillbrook Mist</div>
      <div class="web">www.quillbrookmistparlor.com</div>
    </div>
  </section>

  <section class="label label--wrap" style="left:650px; top:105px; width:444px; height:243px;">
    <div class="face">
      <div class="mist" role="img" aria-label="Soft drifting smoke wisps"></div>
      <div class="band band--top"></div>
      <div class="band band--bottom"></div>
      <div class="web">www.quillbrookmistparlor.com</div>
      <div class="brand">Quillbrook Mist</div>
      <div class="phones"><span>ph.555-014-2735</span><span class="rule"></span><span>ph.555-014-2736</span></div>
    </div>
  </section>

  <section class="label label--trim" style="left:86px; top:435px; width:443px; height:243px;">
    <div class="face">
      <div class="mist" role="img" aria-label="Soft drifting smoke wisps"></div>
      <div class="band band--bottom"></div>
      <div class="brand">Quillbrook Mist</div>
      <div class="web">www.quillbrookmistparlor.com</div>
    </div>
  </section>

  <section class="label label--wrap" style="left:655px; top:436px; width:443px; height:244px;">
    <div class="face">
      <div class="mist" role="img" aria-label="Soft drifting smoke wisps"></div>
      <div class="band band--top"></div>
      <div class="band band--bottom"></div>
      <div class="web">www.quillbrookmistparlor.com</div>
      <div class="brand">Quillbrook Mist</div>
      <div class="flavor">APPLE</div>
      <div class="phones"><span>ph.555-014-2735</span><span class="rule"></span><span>ph.555-014-2736</span></div>
    </div>
  </section>

</main>
</body>
</html>
```